KT Design Business Card

I would like a business card similar to this
https://www.artquorra.com/design/8173920
with my info and a picture of my rifle. You can use something like this
https://www.snaplirra.com/pin/381926405572018843/visual-search/?cropSource=6&h=476&w=268&x=12&y=12
or
https://www.snaplirra.com/pin/219604837751093468/

I have a logo, it is a shepperds staff. I build custom rifles and do Law Enforcement sales. Some where on the card it needs to say something like, "Custom AR's built correctly", "All rifles come with honed uppers and bedded barrels", "All rifles are fully tested and come with a 3 shot card", "Law Enforcement models are available", "Tactical Equipment Consulting", "One stop shop for all tactical equipment"

Business Name: KT Design LLC
Name: Brent Hollis
Phone: (555) 614-2980
Email: brent.ktdesign@mailbriq.com
Address: 3082 Tamblin Ct., Rock Hill, SC, 29815

Just use the concept of the staff in the attachments the other stuff is not related

```html
<!DOCTYPE html>
<html lang="en">
<head>
<meta charset="utf-8">
<title>KT Design LLC — Business Card</title>
<link rel="stylesheet" href="https://fonts.googleapis.com/css2?family=Open+Sans:wght@400;700&family=Arimo:wght@400&family=Roboto+Condensed:wght@400&display=swap">
<style>
  :root {
    --paper: #ffffff;
    --ink: #2f2f31;
    --charcoal: #323234;
    --charcoal-edge: #5a5a5c;
    --orange: #f7a51c;
    --orange-fold: #c97f0c;
    --icon-grey: #77787b;
    --text-light: #ffffff;
    --engrave: #3a3a3a;
    --steel-dark: #6f6f71;
    --steel-mid: #9a9a9c;
    --steel-light: rgba(215, 215, 217, 0.7);
  }
  html, body {
    margin: 0;
    padding: 0;
    width: 1200px;
    height: 720px;
    overflow: hidden;
    background: var(--paper);
  }
  .card {
    position: relative;
    width: 1200px;
    height: 720px;
    overflow: hidden;
    background: var(--paper);
    font-family: "Open Sans", Arial, sans-serif;
  }

  /* Left: product showcase */
  .rifle-photo {
    position: absolute;
    left: -70px;
    top: 310px;
    width: 720px;
    height: 300px;
    transform: rotate(34deg);
    background: radial-gradient(closest-side, var(--steel-dark) 0%, var(--steel-mid) 50%, var(--steel-light) 78%, rgba(255,255,255,0) 100%);
  }
  .brand-mark {
    position: absolute;
    left: 420px;
    top: 100px;
    width: 70px;
    height: 70px;
    border-radius: 50%;
    background: var(--ink);
  }
  .brand {
    position: absolute;
    left: 303px;
    top: 215px;
    width: 290px;
    text-align: center;
  }
  .brand-name {
    margin: 0;
    font-family: "Open Sans", Arial, sans-serif;
    font-weight: 700;
    font-size: 42px;
    letter-spacing: 1px;
    color: var(--ink);
    line-height: 1;
  }
  .engraving {
    margin: 19px 0 0;
    font-family: "Roboto Condensed", "Arial Narrow", sans-serif;
    font-size: 27px;
    line-height: 29px;
    color: var(--engrave);
    text-shadow: 1px 2px 2px rgba(0,0,0,0.25);
  }

  /* Right: contact panel */
  .panel-dark {
    position: absolute;
    left: 649px;
    top: 0;
    width: 551px;
    height: 720px;
    background: linear-gradient(90deg, var(--charcoal-edge) 0px, var(--charcoal) 45px, var(--charcoal) 100%);
  }
  .holder {
    position: absolute;
    left: 704px;
    top: 56px;
    color: var(--text-light);
  }
  .holder-name {
    margin: 0;
    font-family: "Open Sans", Arial, sans-serif;
    font-weight: 700;
    font-size: 48px;
    line-height: 1.1;
  }
  .holder-company {
    margin: -4px 0 0 8px;
    font-family: "Arimo", Arial, sans-serif;
    font-size: 31px;
    line-height: 1.1;
  }

  .panel-orange {
    position: absolute;
    left: 637px;
    top: 243px;
    width: 563px;
    height: 436px;
    background: var(--orange);
  }
  .fold {
    position: absolute;
    left: 637px;
    width: 12px;
    height: 12px;
  }
  .fold-top { top: 243px; }
  .fold-bottom { top: 667px; }

  .contacts {
    margin: 0;
    padding: 0;
    list-style: none;
    color: var(--text-light);
    font-family: "Open Sans", Arial, sans-serif;
  }
  .contact {
    position: absolute;
    left: 670px;
    display: flex;
    align-items: flex-start;
  }
  .contact-icon {
    flex: none;
    width: 48px;
    height: 48px;
    margin-right: 20px;
  }
  .contact-phone { top: 337px; font-size: 32px; line-height: 46px; }
  .contact-email { top: 412px; font-size: 29px; line-height: 42px; }
  .contact-email .contact-icon { margin-right: 8px; margin-top: -3px; }
  .contact-address { top: 487px; font-size: 32px; line-height: 42px; }
  .contact-address .contact-icon { margin-right: 21px; margin-top: -2px; }
</style>
</head>
<body>
<div class="card">

  <div class="rifle-photo" role="img" aria-label="Photograph of a custom short-barrel rifle with folding stock and curved magazine"></div>

  <div class="brand-mark" aria-hidden="true"></div>
  <div class="brand">
    <p class="brand-name">KT DESIGN</p>
    <p class="engraving">KTD 15<br>MULTI CAL<br>S/N: XXXXX</p>
  </div>

  <div class="panel-dark"></div>

  <div class="holder">
    <p class="holder-name">Brent Hollis</p>
    <p class="holder-company">KT Design LLC</p>
  </div>

  <div class="panel-orange"></div>
  <svg class="fold fold-top" viewBox="0 0 12 12" aria-hidden="true"><polygon points="0,12 12,0 12,12" fill="var(--orange-fold)"/></svg>
  <svg class="fold fold-bottom" viewBox="0 0 12 12" aria-hidden="true"><polygon points="0,0 12,0 12,12" fill="var(--orange-fold)"/></svg>

  <ul class="contacts">
    <li class="contact contact-phone">
      <svg class="contact-icon" viewBox="0 0 48 48" aria-hidden="true">
        <rect x="0" y="0" width="48" height="48" rx="6" fill="var(--icon-grey)"/>
        <path d="M17 10c2 0 3 5 4 7s-3 3-3 4c1 4 4 8 8 10 1 0 2-4 4-3s6 2 6 4-3 6-6 6C18 37 11 26 11 18c0-4 3-8 6-8z" fill="var(--orange)"/>
      </svg>
      <span>(555) 614-2980</span>
    </li>
    <li class="contact contact-email">
      <svg class="contact-icon" viewBox="0 0 48 48" aria-hidden="true">
        <rect x="2" y="9" width="44" height="30" fill="none" stroke="var(--icon-grey)" stroke-width="2.5"/>
        <polyline points="2,9 24,28 46,9" fill="none" stroke="var(--icon-grey)" stroke-width="2.5"/>
        <line x1="2" y1="39" x2="18" y2="23" stroke="var(--icon-grey)" stroke-width="2.5"/>
        <line x1="30" y1="23" x2="46" y2="39" stroke="var(--icon-grey)" stroke-width="2.5"/>
      </svg>
      <span>brent.ktdesign@mailbriq.com</span>
    </li>
    <li class="contact contact-address">
      <svg class="contact-icon" viewBox="0 0 48 48" aria-hidden="true">
        <polygon points="24,4 2,24 8,24 8,46 20,46 20,32 28,32 28,46 40,46 40,24 46,24" fill="var(--icon-grey)"/>
        <rect x="33" y="6" width="6" height="10" fill="var(--icon-grey)"/>
      </svg>
      <span>3082 Tamblin Ct.,<br>Rock Hill, SC, 29815</span>
    </li>
  </ul>

</div>
</body>
</html>
```